" O Instituto VEMA de Educação e Saúde oferece programas de Pós-Graduação para quem quer se aprimorar e se tornar líder em sua área de atuação. Formação completa para aperfeiçoar suas habilidades e competências. Nossos programas de especialização oferecem a oportunidade de aprender com a excelência na estrutura do ensino-aprendizagem e corpo docente de profissionais referência no mercado e nas áreas de especialização que atuam. Metodologias ativas, tecnológicas e inovadoras que conduzem seus projetos e pesquisas ao melhor resultado e desenvolvimento da sua carreira. "

```html
<!DOCTYPE html>
<html lang="pt-BR">
<head>
<meta charset="utf-8">
<title>Pasta – Instituto VEMA</title>
<link rel="stylesheet" href="https://fonts.googleapis.com/css2?family=Josefin+Sans:wght@300;400;600&family=Montserrat:wght@400;600&display=swap">
<style>
  :root{
    --board:#9dd0cf;
    --navy:#0c3d72;
    --gold:#c9a15a;
    --white:#ffffff;
  }
  *{margin:0;padding:0;box-sizing:border-box}
  html,body{width:1200px;height:1200px;overflow:hidden;background:var(--board)}
  .board{position:relative;width:1200px;height:1200px;background:var(--board)}
  .board-title{
    position:absolute;top:80px;left:0;width:100%;text-align:center;
    font-family:"Josefin Sans",sans-serif;font-weight:600;font-size:34px;
    letter-spacing:2px;color:var(--white);
  }
  .folder{position:absolute;left:0;top:0;width:1200px;height:1200px}
  .watermark{
    position:absolute;left:300px;top:300px;white-space:nowrap;
    font-family:"Josefin Sans",sans-serif;font-weight:300;font-size:260px;
    color:rgba(255,255,255,0.05);letter-spacing:10px;
  }
  .brand-main{position:absolute;left:660px;top:470px;width:480px;text-align:center}
  .brand-main .brand-dot{width:26px;height:26px;border-radius:50%;background:var(--gold);margin:0 auto 60px}
  .brand-name{
    font-family:"Josefin Sans",sans-serif;font-weight:400;color:var(--white);
    font-size:54px;line-height:1;white-space:nowrap;
  }
  .brand-sub{
    font-family:"Josefin Sans",sans-serif;font-weight:400;color:var(--gold);
    font-size:20px;letter-spacing:5px;margin-top:6px;white-space:nowrap;
  }
  .brand-small{position:absolute;left:236px;top:726px}
  .brand-small .brand-name{font-size:28px}
  .brand-small .brand-sub{font-size:9px;letter-spacing:2.5px;margin-top:2px;text-align:right}
  .contacts{
    position:absolute;left:108px;top:790px;display:flex;gap:22px;list-style:none;
    font-family:"Montserrat",sans-serif;font-size:10px;line-height:14px;color:var(--white);
    white-space:nowrap;
  }
  .contact{display:flex;align-items:center;gap:6px}
  .contact svg{width:14px;height:14px}
</style>
</head>
<body>
<main class="board">
  <h1 class="board-title">PASTA</h1>

  <svg class="folder" viewBox="0 0 1200 1200" aria-hidden="true">
    <defs>
      <linearGradient id="goldBand" x1="0" x2="1">
        <stop offset="0" stop-color="#a87a35"/>
        <stop offset="0.5" stop-color="#f6e2ae"/>
        <stop offset="1" stop-color="#c9a15a"/>
      </linearGradient>
      <linearGradient id="flapGold" x1="0" x2="1">
        <stop offset="0" stop-color="#f6e6bd"/>
        <stop offset="0.6" stop-color="#e2c486"/>
        <stop offset="1" stop-color="#c09049"/>
      </linearGradient>
      <filter id="shadow" x="-5%" y="-5%" width="110%" height="120%">
        <feDropShadow dx="0" dy="6" stdDeviation="6" flood-color="#000" flood-opacity="0.25"/>
      </filter>
    </defs>
    <rect class="folder-cover" x="77" y="192" width="1046" height="700" fill="var(--navy)" filter="url(#shadow)"/>
    <path class="gold-wave" d="M77 868 C 400 850, 700 800, 1123 792 L1123 804 C 700 810, 420 862, 77 882 Z" fill="url(#goldBand)"/>
    <path class="folder-pocket" d="M77 882 C 250 870, 420 856, 570 848 Q 600 848 600 878 L600 1128 L77 1128 Z" fill="url(#flapGold)" filter="url(#shadow)"/>
  </svg>

  <div class="watermark">VEMA</div>

  <div class="brand-main">
    <div class="brand-dot"></div>
    <div class="brand-name">Instituto VEMA</div>
    <div class="brand-sub">PÓS GRADUAÇÃO</div>
  </div>

  <div class="brand-small">
    <div class="brand-name">Instituto VEMA</div>
    <div class="brand-sub">PÓS GRADUAÇÃO</div>
  </div>

  <ul class="contacts">
    <li class="contact"><svg viewBox="0 0 16 16"><circle cx="8" cy="8" r="7" fill="none" stroke="#fff" stroke-width="1.4"/></svg>(11) 90000-0000</li>
    <li class="contact"><svg viewBox="0 0 16 16"><circle cx="8" cy="8" r="7" fill="none" stroke="#fff" stroke-width="1.4"/></svg>@institutovema</li>
    <li class="contact"><svg viewBox="0 0 16 16"><path d="M8 1.5a4.5 4.5 0 0 0-4.5 4.5c0 3.4 4.5 8.5 4.5 8.5s4.5-5.1 4.5-8.5A4.5 4.5 0 0 0 8 1.5z" fill="none" stroke="#fff" stroke-width="1.4"/><circle cx="8" cy="6" r="1.6" fill="#fff"/></svg>vema.edu.br</li>
    <li class="contact"><svg viewBox="0 0 16 16"><rect x="1.5" y="3.5" width="13" height="9" fill="none" stroke="#fff" stroke-width="1.4"/><path d="M1.5 3.5 8 9l6.5-5.5" fill="none" stroke="#fff" stroke-width="1.4"/></svg>contato@vema.edu.br</li>
  </ul>
</main>
</body>
</html>
```